" Não vendemos nossos serviços "no varejo". Somos chamados a participar de projetos de investimento no Brasil ainda na fase de concepção, sob acordo de confidencialidade, buscando alimentar a modelagem financeira com os inputs tributários que frequentemente são cruciais na definição de viabilidade do projeto. Também somos chamados por nossos clientes para avaliar ou alocar contratualmente riscos decorrentes de contingências fiscais, especialmente em fusões e aquisições de empresas. E, ainda, patrocinar defesas ou pleitos em processos administrativos ou judiciais, sempre tendo como parte adversária o fisco (federal, estadual ou municipal). Atuamos em um ambiente profissional onde ética, compliance, qualidade e comprometimento são premissas. O propósito de nossa empresa é a criação de valor de modo sustentável, em questões fiscais, para negócios empreendidos no Brasil. "

```html
<!DOCTYPE html>
<html lang="pt-BR">
<head>
<meta charset="utf-8">
<title>Ferraz Lopes Teixeira Advogados — Papelaria</title>
<link href="https://fonts.googleapis.com/css2?family=Montserrat:wght@400;500;600&display=swap" rel="stylesheet">
<style>
  :root{
    --bg:#e9eaec;
    --paper:#ffffff;
    --navy:#1f2a5c;
    --blue:#2f5f9f;
    --blue-soft:#6f8fbf;
    --grey-text:#8a93a3;
    --faint:#eceef2;
    --line:#c9d3e3;
  }
  *{box-sizing:border-box;margin:0;padding:0}
  html,body{width:1200px;height:1200px;overflow:hidden;background:var(--bg);font-family:"Montserrat",sans-serif}
  .stage{position:relative;width:1200px;height:1200px}

  .envelope{position:absolute;left:60px;top:330px;width:540px;height:560px;background:var(--paper);box-shadow:0 6px 24px rgba(0,0,0,.12);overflow:hidden}
  .envelope__flap{position:absolute;left:0;top:0;width:540px;height:110px}
  .envelope__flap-name{position:absolute;top:24px;left:0;width:540px;text-align:center;color:#fff;font-weight:500;font-size:22px;letter-spacing:4px}
  .envelope__ghost{position:absolute;left:54px;top:205px;color:var(--faint);font-weight:500;font-size:118px;letter-spacing:8px;line-height:1}
  .envelope__edge{position:absolute;left:0;top:468px;width:6px;height:70px;background:var(--blue)}
  .contact{position:absolute;left:28px;top:470px;list-style:none;font-size:9.5px;color:var(--grey-text);line-height:13px}
  .contact li{display:flex;align-items:flex-start;gap:7px;margin-bottom:3px}
  .contact svg{flex:none;margin-top:1px}
  .contact__rule{position:absolute;left:28px;top:548px;width:300px;height:1px;background:var(--line)}
  .signature{position:absolute;left:360px;top:468px;display:flex;gap:14px;align-items:flex-start}
  .signature__stack{font-size:11px;letter-spacing:1.5px;color:var(--blue-soft);line-height:14px;text-transform:uppercase;border-left:1px solid var(--line);padding-left:8px}
  .signature__name{font-size:14px;font-weight:500;color:var(--navy);letter-spacing:2px;margin-top:12px}

  .folder{position:absolute;left:660px;top:260px;width:470px;height:680px;background:var(--paper);box-shadow:0 6px 24px rgba(0,0,0,.12);overflow:hidden}
  .folder__name{position:absolute;top:250px;left:0;width:100%;text-align:center;color:var(--navy);font-weight:500;font-size:28px;letter-spacing:6px;line-height:1.35}
  .folder__rule{position:absolute;left:0;width:100%;background:var(--blue)}
  .folder__rule--thin{top:608px;height:2px;background:var(--blue-soft)}
  .folder__rule--band{top:618px;height:12px}
</style>
</head>
<body>
<main class="stage">

  <section class="envelope" aria-label="Envelope">
    <svg class="envelope__flap" viewBox="0 0 540 110" aria-hidden="true">
      <path d="M0 0H540V62H80Q50 62 40 80Q28 104 0 104Z" fill="var(--blue)"/>
    </svg>
    <div class="envelope__flap-name">FLT</div>

    <div class="envelope__ghost" aria-hidden="true">FLT<br>FLT</div>

    <div class="envelope__edge"></div>
    <ul class="contact">
      <li>
        <svg width="9" height="9" viewBox="0 0 10 10"><circle cx="5" cy="5" r="4.5" fill="var(--blue)"/></svg>
        (21) 3049-7720
      </li>
      <li>
        <svg width="9" height="9" viewBox="0 0 10 10"><circle cx="5" cy="5" r="4.5" fill="var(--blue)"/></svg>
        <span>Rua Almirante Saddock 210, 5º andar<br>Leblon - Rio de Janeiro - RJ<br>CEP 22431-040</span>
      </li>
      <li>
        <svg width="9" height="9" viewBox="0 0 10 10"><circle cx="5" cy="5" r="4.5" fill="var(--blue)"/></svg>
        fltadv.com.br
      </li>
    </ul>
    <div class="contact__rule"></div>

    <div class="signature">
      <div class="signature__stack">Ferraz<br>Lopes<br>Teixeira<br>Advogados</div>
      <div class="signature__name">FLT</div>
    </div>
  </section>

  <section class="folder" aria-label="Pasta">
    <div class="folder__name">FERRAZ LOPES<br>TEIXEIRA</div>
    <div class="folder__rule folder__rule--thin"></div>
    <div class="folder__rule folder__rule--band"></div>
  </section>

</main>
</body>
</html>
```